Coffee House With Cycling Theme Wants Business Cards

We want to create a business card for a coffee house that has a cycling theme. We expect to use the current logo on one side of the business card and we have been considering adding the words 'COFFEE HOUSE' underneath (see example). For the other side of the business card we want an interesting design with tag-line, address and social media links (the normal business card stuff). See examples provided but we are not fixed on having it exactly as shown, we are very open to great creative ideas. Please note our logo has the initials ‘RM' in orange embedded in the design and this must be retained. However, you can play with the words COFFEE HOUSE as well as use the orange color on the backside of the business card, as you see fit. For an image on the backside of the business card it can be a photo, hand-drawn or whatever but it must visually combine coffee and cycling in some way. The interior of the Coffee House will be reclaimed wood, rustic and have an urban feel to it with cycling artifacts hanging from the walls/ceiling, etc. Finally, it would be beneficial if the business card design elements can be easily used on flyers and other promotional assets. Good luck, we are looking forward to seeing your creative ideas.

Target Market(s)

Coffee lovers and cycling fans

Contact Information for Business Card

See project description.

Colors

Designer to choose colors to be used in the design.

Requirements
Must have
• Must use the current logo provided and combine a coffee and bike theme.
Nice to have
• Orange is used in current logo and could be used as an accent color on the backside of the business card.

```html
<!DOCTYPE html>
<html lang="en">
<head>
<meta charset="utf-8">
<title>RM Coffee House – Business Card</title>
<link href="https://fonts.googleapis.com/css2?family=Courier+Prime:wght@400;700&display=swap" rel="stylesheet">
<style>
  :root {
    --charcoal: #3d3d3d;
    --orange: #f1672a;
    --white: #ffffff;
    --blush: #e9c6b6;
    --latte: #b67c4a;
  }
  * { margin: 0; padding: 0; box-sizing: border-box; }
  html, body { width: 960px; height: 1200px; overflow: hidden; background: var(--white); }
  body { position: relative; font-family: "Courier Prime", "Courier New", monospace; }

  .card { position: absolute; left: 0; width: 960px; overflow: hidden; }
  .card-front { top: 0; height: 559px; background: var(--charcoal); }
  .card-back { top: 640px; height: 560px; background: var(--charcoal); }
  .card-art { position: absolute; inset: 0; width: 100%; height: 100%; display: block; }

  .brand-mark {
    position: absolute; left: 0; width: 960px; top: 150px;
    text-align: center; color: var(--orange);
    font-weight: 700; font-size: 180px; line-height: 1; letter-spacing: 4px;
  }
  .brand-name {
    position: absolute; left: 0; width: 960px; top: 358px;
    text-align: center; color: var(--orange);
    font-size: 48px; line-height: 1; letter-spacing: 1px;
  }

  .tagline {
    position: absolute; left: 62px; top: 58px;
    color: var(--orange); font-size: 45px; line-height: 1;
  }
  .contact {
    position: absolute; display: flex; align-items: flex-end; gap: 14px;
    color: var(--charcoal); font-size: 28px; line-height: 1;
  }
  .contact-square { width: 51px; height: 51px; border-radius: 7px; background: var(--charcoal); flex: none; }
  .contact-circle { width: 48px; height: 48px; border-radius: 50%; border: 3px solid var(--charcoal); flex: none; }
  .contact-social-primary { left: 402px; top: 171px; }
  .contact-social-secondary { left: 251px; top: 247px; }
  .contact-web { left: 140px; top: 326px; gap: 11px; }

  .address {
    position: absolute; left: 63px; top: 450px;
    display: flex; gap: 8px; color: var(--charcoal);
  }
  .address-pin { width: 34px; height: 50px; flex: none; margin-top: 10px; }
  .address-lines { font-size: 28px; line-height: 38px; }
  .address-lines span { display: block; }
  .address-lines .street { padding-left: 24px; }

  .cup-illustration {
    position: absolute; left: 620px; top: 296px; width: 276px; height: 204px;
    border-radius: 50%;
    background: radial-gradient(ellipse at 45% 45%, var(--latte) 0%, var(--charcoal) 55%, rgba(241,103,42,0) 72%);
    opacity: .8;
  }
</style>
</head>
<body>

<section class="card card-front" aria-label="Card front">
  <svg class="card-art" viewBox="0 0 1134 660" preserveAspectRatio="none" aria-hidden="true">
    <defs>
      <linearGradient id="front-fringe-left" x1="0" y1="0" x2="1" y2="0">
        <stop offset="0" stop-color="#e4b8a3"/>
        <stop offset="1" stop-color="#ffffff"/>
      </linearGradient>
      <linearGradient id="front-fringe-right" x1="1" y1="0" x2="0" y2="0">
        <stop offset="0" stop-color="#ffffff"/>
        <stop offset="1" stop-color="#e4b8a3"/>
      </linearGradient>
    </defs>
    <path fill="var(--orange)" d="M0,360 C110,215 300,120 460,80 C650,35 820,12 960,0 L1134,0 L1134,300 C1080,420 900,530 690,580 C480,630 250,650 0,660 Z"/>
    <path fill="url(#front-fringe-left)" d="M0,530 C40,380 130,240 300,150 C320,140 340,132 360,124 C220,220 110,400 30,660 L0,660 Z"/>
    <path fill="url(#front-fringe-right)" d="M1110,0 L1134,0 C1100,170 1020,330 850,495 C960,350 1060,200 1110,0 Z"/>
    <path fill="var(--white)" d="M30,660 C90,420 180,250 320,150 C520,70 800,22 1100,0 C1060,170 980,340 850,490 C720,590 450,640 180,660 Z"/>
  </svg>
  <div class="brand-mark">RM</div>
  <div class="brand-name">COFFEE HOUSE</div>
</section>

<section class="card card-back" aria-label="Card back">
  <svg class="card-art" viewBox="0 0 1134 662" preserveAspectRatio="none" aria-hidden="true">
    <defs>
      <linearGradient id="back-fringe" x1="0" y1="1" x2="1" y2="0">
        <stop offset="0" stop-color="#ffffff"/>
        <stop offset="0.5" stop-color="#f1d2c4"/>
        <stop offset="1" stop-color="#f6ddd2"/>
      </linearGradient>
    </defs>
    <path fill="url(#back-fringe)" d="M0,470 C150,300 400,190 700,115 C900,65 1050,35 1134,22 L1134,32 C900,80 600,160 380,280 C200,380 80,480 0,560 Z"/>
    <path fill="var(--orange)" d="M0,560 C120,420 280,310 480,230 C700,140 950,70 1134,28 L1134,662 L0,662 Z"/>
  </svg>

  <p class="tagline">Brew the Ride</p>

  <div class="contact contact-social-primary">
    <span class="contact-square" aria-hidden="true"></span>
    <span class="contact-handle">rmcoffeehouse</span>
  </div>
  <div class="contact contact-social-secondary">
    <span class="contact-square" aria-hidden="true"></span>
    <span class="contact-handle">rmcoffeehouse</span>
  </div>
  <div class="contact contact-web">
    <span class="contact-circle" aria-hidden="true"></span>
    <span class="contact-handle">rmcoffeehouse.com</span>
  </div>

  <div class="address">
    <svg class="address-pin" viewBox="0 0 34 50" aria-hidden="true">
      <path fill="var(--charcoal)" d="M17,0 C7.6,0 0,7.6 0,17 C0,29 17,50 17,50 C17,50 34,29 34,17 C34,7.6 26.4,0 17,0 Z"/>
      <circle cx="17" cy="16" r="8" fill="var(--orange)"/>
    </svg>
    <p class="address-lines">
      <span class="street">4820 Finch Lane</span>
      <span class="city">Oceanside, California</span>
    </p>
  </div>

  <div class="cup-illustration" role="img" aria-label="Line illustration of a steaming coffee cup on a saucer with a second saucer beside it"></div>
</section>

</body>
</html>
```